Webdesign für Augenarztpraxis gesucht
Zielgruppe
Augenarztpraxis, Zielgruppe: Patienten, Interessenten
Aufgabenstellung
Liebe Designer, liebe Designerinnen,
es handelt sich hierbei um keinen Design-Contest, eher um eine Ausschreibung.
anbei die konkrete Projektinalte:
- bestehende HP http://www.sehzentrum-lindmoor.de moderner gestalten
- Aufbau und Inhalte können übernommen werden, nur Austausch von alten Bildern (Fotoshooting geplant)
- ergänzend: Bildlizenzen / Stockfotografie
- Aufbau aller Seiten und Unterseiten
- SEO/SEA Googleanpassungen – Implementierung relevanter Suchbegriffe
- eventuell kleine Textanpassungen
- gehostetes CMS, geringe Wartungskosten
- DSGVO konformes Impressum und Datenschutzseite
- Technische Abwicklung mit dem Hoster
Bitte um Nennung der Kosten (siehe oben):
- Gesamtkosten Umgestaltung der HP
- Kosten CMS Hosting
- sonstige Wartungskosten
- Stundensatz für sonstige Programmierleistungen
- Stundensatz für das Sichten der gelieferten Texte, anpassen und Neuanpassung der Texte pro Seite
Wichtig: bitte geben Sie Referenzen an, um die Vorauswahl zu erleichtern
Vielen Dank!
brunowaldau@postfeld.de
- es soll die bestehende HP: http://blickhaus-falkenau.de/team.html moderner gestaltet werden
- die meißten Inhalte können von der aktuellen HP: http://blickhaus-falkenau.de/team.html übernommen werden
- neue Praxis- und Mitarbeiterfotos werden durch einen Fotografen neu erstellt (Auftrag ist noch zu vergeben)
- Wichtig: bitte geben Sie unbedingt Referenzen an, um die Vorauswahl zu erleichtern
- bitte auch um die Angabe von Preisen für spätere Änderungen bezügl. Inhalte und Aufbau

```html
<!DOCTYPE html>
<html lang="de">
<head>
<meta charset="utf-8">
<title>Augenklinik Falkenau</title>
<link href="https://fonts.googleapis.com/css2?family=Source+Sans+3:wght@400;600;700&display=swap" rel="stylesheet">
<style>
:root{
  --navy:#22234f;
  --ink:#1d1d1f;
  --muted:#7a7a7a;
  --white:#ffffff;
  --line:#d6d6d6;
}
*{box-sizing:border-box;margin:0;padding:0}
html,body{width:899px;height:1200px;overflow:hidden;background:var(--white)}
body{position:relative;font-family:"Source Sans 3",sans-serif;color:var(--ink)}
.abs{position:absolute}
.topbar{left:4px;right:4px;top:3px;height:6px;background:var(--navy)}
.navbar-line{left:4px;right:4px;top:178px;height:4px;background:var(--navy)}
.header{left:4px;right:4px;top:9px;height:169px;box-shadow:0 2px 4px rgba(0,0,0,.15)}
.brand{left:124px;top:28px;display:flex;align-items:center;gap:9px}
.brand-dot{width:26px;height:26px;border-radius:50%;background:var(--navy)}
.brand-name{font-size:26px;font-weight:700;color:var(--ink);letter-spacing:.3px}
.doctors{left:165px;top:62px;font-size:12.5px;letter-spacing:.6px;line-height:20.5px;text-transform:uppercase}
.nav{left:0;top:146px;width:899px;height:32px}
.nav a{position:absolute;top:0;height:32px;line-height:34px;font-size:11.5px;letter-spacing:.6px;color:var(--ink);text-decoration:none}
.nav a.active{background:var(--navy);color:var(--white);border-radius:2px 2px 0 0;width:78px;text-align:center}
h2{position:absolute;left:165px;font-size:17px;font-weight:600;letter-spacing:.3px}
.intro{left:165px;top:266px;width:357px;font-size:12px;line-height:17.7px;text-align:justify}
.cta{left:163px;top:398px;width:257px;height:35px;background:var(--navy);color:var(--white);font-size:13.5px;font-weight:600;letter-spacing:.3px;line-height:35px;padding-left:11px;border-radius:1px;box-shadow:0 1px 3px rgba(0,0,0,.3)}
.cta .caret{position:absolute;right:10px;top:0;font-size:7px}
.card{left:564px;width:171px;background:var(--white);box-shadow:0 1px 3px rgba(0,0,0,.28);border-radius:2px;overflow:hidden}
.card-head{background:var(--navy);color:var(--white);text-align:center;font-size:15px;font-weight:600;letter-spacing:.3px;height:35px;line-height:35px}
.hours{padding:8px 12px 0;font-size:12px;line-height:16.8px}
.hours .row{display:flex}
.hours b{width:58px;font-weight:600}
.hours .gap{height:16px}
.hours .note{font-weight:600;margin-top:14px;letter-spacing:-.2px}
.address{text-align:center;font-size:12px;font-weight:600;line-height:16.8px;padding:8px 0}
.acc{left:163px;height:35px;background:var(--white);box-shadow:0 1px 3px rgba(0,0,0,.28);border-radius:1px;font-size:13px;letter-spacing:.3px;line-height:35px;padding-left:11px}
.acc.open{background:var(--navy);color:var(--white);box-shadow:none}
.acc .arrow{position:absolute;right:14px;top:15px;width:0;height:0;border-left:3px solid transparent;border-right:3px solid transparent;border-top:3.5px solid currentColor}
.acc.open .arrow{border-top:none;border-bottom:3.5px solid currentColor;top:14px}
.acc-body{left:163px;top:708px;width:354px;height:67px;background:var(--white);box-shadow:0 1px 3px rgba(0,0,0,.28);padding:8px 11px;font-size:11px;line-height:17.6px;text-align:justify}
.acc-body .more{position:absolute;right:10px;bottom:8px;font-size:7px;color:var(--muted);line-height:1}
</style>
</head>
<body>
<div class="abs header"></div>
<div class="abs topbar"></div>
<div class="abs brand"><span class="brand-dot"></span><span class="brand-name">AUGENKLINIK FALKENAU</span></div>
<div class="abs doctors">Priv.-Doz. Dr. Henrik Almstedt<br>Dr. Marlene Obertal<br>Dr. Svenja Almstedt</div>
<nav class="abs nav">
  <a style="left:165px">Home</a>
  <a style="left:255px">Leistungen</a>
  <a style="left:373px">Diagnosen</a>
  <a class="active" style="left:464px">Team</a>
  <a style="left:576px">Kontakt</a>
  <a style="left:676px">Impressum</a>
</nav>
<div class="abs navbar-line"></div>

<h2 style="top:216px">Herzlich Willkommen</h2>
<p class="abs intro">Seit unserem Bestehen haben wir weit über 55.000 Operationen mit höchster Präzision durchgeführt. Dabei ist selbstverständlich unser oberstes Ziel die Zufriedenheit unserer Patientinnen und Patienten. Nach einer ausführlichen Diagnostik mit modernsten Geräten und einer individuellen Beratung führen wir ambulante Operationen und Behandlungen in einem breiten Spektrum durch.</p>
<div class="abs cta">Vereinbaren Sie direkt einen Termin<span class="caret">&#9654;</span></div>

<section class="abs card" style="top:268px;height:165px">
  <div class="card-head">Sprechzeiten</div>
  <div class="hours">
    <div class="row"><b>Mo. - Fr.:</b><span>08:00 - 12:00 Uhr</span></div>
    <div class="row"><b>Mo. - Do.:</b><span>15:00 - 17:00 Uhr</span></div>
    <div class="gap"></div>
    <div class="row"><b>Telefon:</b><span>04711-380 52</span></div>
    <div class="row"><b>Fax:</b><span>04711-294 730</span></div>
    <div class="note">Termine nach Vereinbarung</div>
  </div>
</section>
<section class="abs card" style="top:443px;height:81px">
  <div class="card-head">Adresse</div>
  <div class="address">Lindenallee 12-14<br>27318 Falkenau</div>
</section>

<h2 style="top:557px">Diagnosen, die Sie kennen sollten</h2>
<div class="abs acc" style="top:605px;width:190px">Grauer Star (Cateract)<span class="arrow"></span></div>
<div class="abs acc open" style="top:673px;width:190px">Grüner Star (Glaukom)<span class="arrow"></span></div>
<div class="abs acc-body">Eine Glaukom-Erkrankung (historisch: Grüner Star) liegt vor, wenn der Sehnerv fortschreitend an Nervenzell-Substanz und damit auch an Funktion verliert.<span class="more">Mehr erfahren &#8250;</span></div>
<div class="abs acc" style="top:809px;width:190px">Kurz-/ Weitsichtigkeit<span class="arrow"></span></div>

<h2 style="top:902px">Unsere Leistungen im Überblick</h2>
<div class="abs acc" style="top:961px;width:371px">Ambulante Operationen<span class="arrow"></span></div>
<div class="abs acc" style="top:1029px;width:371px">Intravitreale operative Medikamenteneingabe (IVOM)<span class="arrow"></span></div>
</body>
</html>
```